Visitenkarten-Design für Süßigkeiten-Onlineshop
Zielgruppe
Ich werde einen Onlineshop betreiben und Süßigkeiten aus aller Welt verkaufen.
Aufgabenstellung
Mein Logo sollte drauf sein. Die Visitenkarte kann auch bisschen stylischer gestaltet werden. Aber da lasse ich mich auch gerne überraschen.
Man könnte vielleicht noch den Slogan- Süßigkeiten aus aller Welt-
Mein Name sollte drauf stehen,
Jonas Brettel
Lindauer Weg 14
41562 Elmsried
E-Mail info@zuckerfuchs-shop.de
Fotoprofil @zuckerfuchs.de
Profilseite Zuckerfuchs
Kurzvideo @zuckerfuhcs.de

```html
<!DOCTYPE html>
<html lang="de">
<head>
<meta charset="utf-8">
<title>Zuckerfuchs – Visitenkarte</title>
<link href="https://fonts.googleapis.com/css2?family=Poppins:wght@400;500;600&display=swap" rel="stylesheet">
<style>
  :root {
    --page: #eeeeee;
    --charcoal: #3f4346;
    --teal: #80c3c8;
    --paper: #fdf9fa;
    --white: #ffffff;
  }
  * { margin: 0; padding: 0; box-sizing: border-box; }
  html, body { width: 1200px; height: 900px; overflow: hidden; background: var(--page); }
  body { position: relative; font-family: "Poppins", sans-serif; }

  .card {
    position: absolute;
    left: 258px;
    width: 684px;
    height: 391px;
    box-shadow: 0 3px 6px rgba(0,0,0,0.28);
    overflow: hidden;
    background: var(--charcoal);
  }
  .card--front { top: 51px; }
  .card--back { top: 458px; }

  .front__brand {
    position: absolute; left: 0; top: 12px;
    width: 342px; height: 367px;
    background: var(--paper);
  }
  .front__pattern { position: absolute; inset: 0; background: linear-gradient(180deg, #fdf6f8, #fbfcfc); }

  .brand-mark {
    position: absolute; left: 0; right: 0;
    display: flex; flex-direction: column; align-items: center;
  }
  .brand-mark__dot { border-radius: 50%; }
  .brand-mark__name { font-weight: 500; text-transform: uppercase; line-height: 1.5; }

  .front__brand .brand-mark { top: 77px; }
  .front__brand .brand-mark__dot { width: 144px; height: 144px; background: var(--teal); }
  .front__brand .brand-mark__name { margin-top: 11px; font-size: 28px; letter-spacing: 4px; color: var(--charcoal); }

  .front__info {
    position: absolute; left: 342px; top: 12px;
    width: 342px; height: 367px;
    background: var(--teal);
    color: var(--white);
  }
  .front__name {
    position: absolute; left: 29px; top: 62px;
    font-size: 31px; line-height: 40px; font-weight: 600; letter-spacing: 0.2px;
  }
  .contact { position: absolute; left: 0; top: 124px; list-style: none; }
  .contact__row {
    position: relative; height: 30.5px;
    padding-left: 66px;
    font-size: 16px; line-height: 30.5px; font-weight: 400;
    white-space: nowrap;
  }
  .contact__icon { position: absolute; left: 26px; top: 5px; width: 20px; height: 20px; }

  .card--back .brand-mark { top: 70px; }
  .card--back .brand-mark__dot { width: 176px; height: 176px; background: var(--white); }
  .card--back .brand-mark__name { margin-top: 5px; font-size: 36px; letter-spacing: 5px; color: var(--white); }
</style>
</head>
<body>

  <section class="card card--front" aria-label="Visitenkarte Vorderseite">
    <div class="front__brand">
      <div class="front__pattern" role="img" aria-label="Zartes Muster aus rosa und türkisen Lutschern"></div>
      <div class="brand-mark">
        <div class="brand-mark__dot"></div>
        <p class="brand-mark__name">Zuckerfuchs</p>
      </div>
    </div>

    <div class="front__info">
      <h1 class="front__name">JONAS BRETTEL</h1>
      <ul class="contact">
        <li class="contact__row">
          <svg class="contact__icon" viewBox="0 0 20 20" aria-hidden="true"><path d="M10 1a7 7 0 0 0-7 7c0 5 7 11 7 11s7-6 7-11a7 7 0 0 0-7-7zm0 9.5a2.5 2.5 0 1 1 0-5 2.5 2.5 0 0 1 0 5z" fill="#fff"/></svg>
          Lindauer Weg 14
        </li>
        <li class="contact__row">41562 Elmsried</li>
        <li class="contact__row">
          <svg class="contact__icon" viewBox="0 0 20 20" aria-hidden="true"><path d="M5.5 1.5l3 3.5-1.8 2.2a11 11 0 0 0 6.1 6.1l2.2-1.8 3.5 3-2 3c-8 0-15-7-15-15z" fill="#fff"/></svg>
          015236908471
        </li>
        <li class="contact__row">
          <svg class="contact__icon" viewBox="0 0 20 20" aria-hidden="true"><circle cx="10" cy="10" r="8.5" fill="none" stroke="#fff" stroke-width="1.6"/></svg>
          Fotoprofil @zuckerfuchs.de
        </li>
        <li class="contact__row">
          <svg class="contact__icon" viewBox="0 0 20 20" aria-hidden="true"><circle cx="10" cy="10" r="8.5" fill="none" stroke="#fff" stroke-width="1.6"/></svg>
          Profilseite Zuckerfuchs
        </li>
        <li class="contact__row">
          <svg class="contact__icon" viewBox="0 0 20 20" aria-hidden="true"><circle cx="10" cy="10" r="8.5" fill="none" stroke="#fff" stroke-width="1.6"/></svg>
          Kurzvideo @zuckerfuhcs.de
        </li>
      </ul>
    </div>
  </section>

  <section class="card card--back" aria-label="Visitenkarte Rückseite">
    <div class="brand-mark">
      <div class="brand-mark__dot"></div>
      <p class="brand-mark__name">Zuckerfuchs</p>
    </div>
  </section>

</body>
</html>
```